IT Services Postcard

I am looking to update and refresh my existing postcard. I would like to keep all the content it has , but make it more modern and elegant. We are a small boutique IT firm here in Miami, FL in business for 15 years. We support all Brelvanta products. I would like highlight that as well on the postcard- "15 years serving South Florida". I would also like to make the following revisions to the bullet points:Change "Included Email & Virus Protection" to Included Antivirus SoftwareChange "Quorvix Pro Remote Control" to "Secure remote computer access"Add the following bullet point "Included Deskora 480 Backup"You can certainly change the images for the bullet points, and refresh the colors and background as well. I have uploaded a copy of the front and back of my last flyer. I target small to medium size businesses who need a good local IT company they can trust. I look forward to working with you. Thank you.
Target Market(s)
Small Businesses
Industry/Entity Type
It Professional
Colors
Designer to choose colors to be used in the design.
Look and feel

```html
<!DOCTYPE html>
<html lang="en">
<head>
<meta charset="utf-8">
<title>Kestran Tech – IT Services Postcard</title>
<link href="https://fonts.googleapis.com/css2?family=Open+Sans:wght@400;600;700;800&display=swap" rel="stylesheet">
<style>
  :root{
    --ink:#1e1e22;
    --blue:#1a78c2;
    --blue-deep:#1565b0;
    --orange:#ee6f1f;
    --icon-bg:#dbe9f5;
    --icon-ring:#7ea6c9;
    --sky:#cfe7f5;
    --band:#6f86c4;
    --lavender:#d6def2;
    --stage:#f1f1f1;
    --badge-grey:#c9ced6;
  }
  *{box-sizing:border-box;margin:0;padding:0}
  html,body{width:1200px;height:1200px;overflow:hidden}
  body{background:var(--stage);font-family:"Open Sans",Arial,sans-serif;color:var(--ink);position:relative}
  .card{position:absolute;left:220px;width:760px;height:538px;overflow:hidden}
  .card--front{top:48px;background:linear-gradient(180deg,var(--sky) 0%,#fff 38%,#fff 100%)}
  .card--back{top:616px;height:536px;background:linear-gradient(160deg,#fafbfe 0%,#e6ebf7 55%,var(--lavender) 100%)}

  .brand{position:absolute;font-weight:800;line-height:1;width:334px}
  .brand__name{display:block;font-size:41px;letter-spacing:0.5px;text-transform:uppercase;color:var(--ink);white-space:nowrap}
  .brand__tag{display:block;font-size:17px;font-weight:800;text-align:right;margin-top:4px;color:var(--ink);white-space:nowrap}
  .card--front .brand{left:22px;top:52px}
  .card--back .brand{left:34px;top:44px}

  .swoosh{position:absolute;left:0;top:0}
  .dashboard{position:absolute;left:470px;top:10px;width:265px;height:290px;border-radius:14px;
    background:linear-gradient(150deg,#f4f7fb 0%,#dfe7ef 55%,#b9c3cc 100%)}

  .includes-title{position:absolute;left:32px;top:144px;font-size:22px;font-weight:700;color:var(--blue);line-height:1.2}
  .features{position:absolute;list-style:none;font-size:12.5px;line-height:1.2}
  .features li{position:absolute;left:0;display:flex;align-items:flex-start;gap:6px}
  .features--left{left:26px;top:0}
  .features--left li{width:200px}
  .features--right{left:238px;top:0}
  .features--right li{width:230px}
  .icon{flex:0 0 26px;width:26px;height:26px;border-radius:50%;background:var(--icon-bg);border:2px solid var(--icon-ring);margin-top:-4px}

  .other-title{position:absolute;left:28px;top:390px;font-size:22px;font-weight:700;color:var(--orange)}
  .other-list{position:absolute;left:28px;top:422px;font-size:10.5px;font-weight:600;white-space:nowrap}
  .other-list span::before{content:"➤";color:var(--blue-deep);margin:0 2px 0 0}

  .years{position:absolute;left:578px;top:322px}

  .cta{position:absolute;left:0;top:444px;width:564px;height:54px;background:var(--orange);
    clip-path:polygon(0 0,552px 0,564px 54px,0 54px);color:#fff;padding:3px 0 0 26px}
  .cta__small{display:block;font-size:16px;font-weight:700;line-height:1}
  .cta__big{display:block;font-size:26px;font-weight:800;line-height:1.15}

  .badges{position:absolute;display:flex;gap:10px;align-items:center}
  .card--front .badges{left:568px;top:456px}
  .card--back .badges{left:36px;top:428px}
  .badge{display:block;height:26px;border-radius:3px}
  .badge--cert{width:54px;background:var(--badge-grey)}
  .badge--specialist{width:54px;background:#2d62b3}
  .badge--partner{width:40px;background:var(--badge-grey)}

  .contact{position:absolute;display:flex;align-items:center;font-size:13px;white-space:nowrap}
  .contact svg{margin-right:6px}
  .contact .item{display:flex;align-items:center;margin-right:26px}
  .card--front .contact{left:39px;top:505px;color:var(--ink)}
  .card--back .contact{left:0;top:490px;width:760px;height:46px;background:var(--band);color:#fff;justify-content:center;font-size:14.5px}
  .card--back .contact .item{margin-right:14px}

  .stamp{position:absolute;left:624px;top:30px;width:82px;height:75px;background:#efeff0}
  .relax{position:absolute;left:444px;top:448px;width:316px;height:42px;background:var(--orange);
    clip-path:polygon(34px 0,316px 0,316px 42px,0 42px);color:#fff;font-size:21px;font-weight:700;
    display:flex;align-items:center;justify-content:flex-end;padding-right:36px}
</style>
</head>
<body>

<section class="card card--front">
  <svg class="swoosh" width="760" height="538" viewBox="0 0 760 538" aria-hidden="true">
    <path d="M378 0 C420 170 560 320 760 330 L760 360 C540 350 395 200 360 0 Z" fill="#9aa0a6"/>
    <path d="M395 0 C445 190 590 310 760 300 L760 355 C560 365 400 220 370 0 Z" fill="var(--blue)"/>
    <path d="M520 300 C600 330 690 320 760 300 L760 340 C680 360 590 350 520 320 Z" fill="#c9ccd1"/>
  </svg>
  <div class="dashboard" role="img" aria-label="Illustration of a desktop monitor showing floating analytics dashboard screens with charts and percentages"></div>

  <div class="brand">
    <span class="brand__name">Kestran Tech</span>
    <span class="brand__tag">MANAGED SERVICES</span>
  </div>

  <h2 class="includes-title">Our Low Cost Monthly<br>IT Service Includes:</h2>

  <ul class="features features--left">
    <li style="top:222px"><span class="icon"></span>24/7 Monitoring of Service</li>
    <li style="top:248px"><span class="icon"></span>Proactive Desktop &amp; Server Maintenance</li>
    <li style="top:284px"><span class="icon"></span>Unlimited Onsite &amp; Remote Support</li>
    <li style="top:320px"><span class="icon"></span>Antivirus Software Change</li>
    <li style="top:344px"><span class="icon"></span>Monthly Network Health Report</li>
  </ul>
  <ul class="features features--right">
    <li style="top:224px"><span class="icon"></span>Secure remote computer<br>access</li>
    <li style="top:263px"><span class="icon"></span>Brelvanta Certified Technicians</li>
    <li style="top:291px"><span class="icon"></span>Fast Response Times</li>
    <li style="top:319px"><span class="icon"></span>No Long Term Contracts</li>
    <li style="top:348px"><span class="icon"></span>Deskora 480 Backup</li>
  </ul>

  <h3 class="other-title">Other Services Offered:</h3>
  <p class="other-list"><span>Onsite/Offside Backup Solution </span><span>Deskora 480 Migration</span><span>Norvale Business Voice Edge Installation</span></p>

  <svg class="years" width="130" height="120" viewBox="0 0 130 120" aria-label="15 years serving South Florida">
    <defs><path id="arc" d="M12 62 A54 54 0 0 0 118 62"/></defs>
    <circle cx="65" cy="50" r="48" fill="var(--blue)"/>
    <circle cx="65" cy="50" r="44" fill="var(--orange)"/>
    <text x="65" y="55" text-anchor="middle" font-family="Open Sans, sans-serif" font-weight="800" font-size="38" fill="#fff">15</text>
    <text x="65" y="80" text-anchor="middle" font-family="Open Sans, sans-serif" font-weight="700" font-size="18" fill="#fff">YEARS</text>
    <text font-family="Open Sans, sans-serif" font-weight="700" font-size="13" fill="var(--ink)"><textPath href="#arc" startOffset="50%" text-anchor="middle">Serving South Florida</textPath></text>
  </svg>

  <div class="cta">
    <span class="cta__small">CALL TODAY AND</span>
    <span class="cta__big">GET 2 FREE HOURS OF ONSITE SERVICE</span>
  </div>
  <div class="badges">
    <span class="badge badge--cert"></span><span class="badge badge--specialist"></span><span class="badge badge--partner"></span>
  </div>

  <div class="contact">
    <span class="item">Contact us Today</span>
    <span class="item"><svg width="16" height="16" viewBox="0 0 16 16"><g fill="none" stroke="var(--orange)" stroke-width="1.2"><circle cx="8" cy="8" r="7"/><ellipse cx="8" cy="8" rx="3" ry="7"/><path d="M1 8h14M2 4.5h12M2 11.5h12"/></g></svg>www.kestrantech.com</span>
    <span class="item"><svg width="16" height="16" viewBox="0 0 16 16"><path d="M3 1l3 3-1.5 2a9 9 0 0 0 5.5 5.5L12 10l3 3-2 2C7 15 1 9 1 3z" fill="var(--orange)"/></svg>305.555.0148</span>
    <span class="item"><svg width="16" height="12" viewBox="0 0 16 12"><g fill="none" stroke="var(--orange)" stroke-width="1.2"><rect x="1" y="1" width="14" height="10"/><path d="M1 1l7 6 7-6"/></g></svg>support@kestrantech.com</span>
  </div>
</section>

<section class="card card--back">
  <div class="brand">
    <span class="brand__name">Kestran Tech</span>
    <span class="brand__tag">MANAGED SERVICES</span>
  </div>
  <div class="stamp"></div>
  <div class="badges">
    <span class="badge badge--cert"></span><span class="badge badge--specialist" style="width:70px;height:34px"></span><span class="badge badge--partner"></span>
  </div>
  <div class="relax">Relax, we can fix IT!</div>
  <div class="contact">
    <span class="item">Contact us Today</span>
    <span class="item"><svg width="17" height="17" viewBox="0 0 16 16"><g fill="none" stroke="#fff" stroke-width="1.2"><circle cx="8" cy="8" r="7"/><ellipse cx="8" cy="8" rx="3" ry="7"/><path d="M1 8h14M2 4.5h12M2 11.5h12"/></g></svg>www.kestrantech.com</span>
    <span class="item"><svg width="17" height="17" viewBox="0 0 16 16"><path d="M3 1l3 3-1.5 2a9 9 0 0 0 5.5 5.5L12 10l3 3-2 2C7 15 1 9 1 3z" fill="#fff"/></svg>305.555.0148</span>
    <span class="item"><svg width="16" height="12" viewBox="0 0 16 12"><g fill="none" stroke="#fff" stroke-width="1.2"><rect x="1" y="1" width="14" height="10"/><path d="M1 1l7 6 7-6"/></g></svg>support@kestrantech.com</span>
  </div>
</section>

</body>
</html>
```